Awesome Professional Template for a collaborative report

File format: A4 PDF ideally

Design Requirements:

3 or 4 variants of a template some with graphics and pull quotes and a bio page for the essayists with a profile pic and a short descriptor

Layout Format: PPT would be perfect ideally portrait format

Style/Reference Guide: Brannick or QV styles thought leadership reports as a guide

We need to input 10 essays around a specific subject with a nice layout with place holders for high impact pull quotes from the copy, stunning colourway and typrography probably A4 format but emailed as a PDF ideally not a huge file size. Striking front cover with title and list of contributors plus layout variations for the essays which will include a head shot short profile and contacts for the authors. Ideally a portrait format PPT that is easy to work with.

Target Market(s)

business professionals in brands

Industry/Entity Type

brand marketing

Font styles to use
Sans Serif

Colors
0054AA
0677BA
7BADD7
CADEEF
E8F1F8
00AB8E
00BBA5
67D7C9
C6EFE9
E9F9F6
F0912C
F2A743
F7CA91
FBE8D2
FDF5EE
6B429C
8869AF
B7A5CE
E3DAEB
F3F0F8

Requirements
Must have
• awesome visual impact

```html
<!DOCTYPE html>
<html lang="en">
<head>
<meta charset="utf-8">
<title>Author Bio – Marlo Quinn</title>
<link href="https://fonts.googleapis.com/css2?family=Montserrat:wght@300;400;500;700&family=Noto+Serif:wght@400&display=swap" rel="stylesheet">
<style>
  :root {
    --ink: #111111;
    --portrait-blue: #1a4c96;
    --portrait-grey: #8a8a8a;
    --footer-navy: #1f3470;
    --accent-purple: #a35cf2;
    --white: #ffffff;
    --book-light: #dfe7f1;
    --book-mid: #7ba6d4;
    --book-deep: #0a3d8c;
  }
  * { margin: 0; padding: 0; box-sizing: border-box; }
  html, body { width: 1200px; height: 676px; overflow: hidden; background: var(--white); }
  .page { position: relative; width: 1200px; height: 676px; overflow: hidden; background: var(--white); font-family: "Montserrat", sans-serif; color: var(--ink); }

  .portrait {
    position: absolute; left: 39px; top: 59px; width: 404px; height: 404px;
    border-radius: 50%;
    background: radial-gradient(ellipse 42% 60% at 46% 62%, var(--portrait-grey) 0 70%, var(--portrait-blue) 71%);
  }

  .name-card {
    position: absolute; left: 64px; top: 478px; width: 341px; height: 97px;
    border: 1.5px solid var(--ink); border-radius: 10px; text-align: center;
  }
  .name-card__name {
    font-family: "Noto Serif", serif; font-weight: 400; font-size: 36px;
    line-height: 1; margin-top: 14px; letter-spacing: -0.3px;
  }
  .name-card__role {
    font-size: 20px; font-weight: 500; letter-spacing: 4px; margin-top: 12px;
  }
  .accent { color: var(--accent-purple); }

  .intro { position: absolute; left: 596px; top: 72px; width: 474px; }
  .intro__title { font-size: 51px; font-weight: 700; line-height: 47px; letter-spacing: -0.3px; }
  .intro__text {
    margin-top: 16px; width: 472px; font-size: 17.5px; font-weight: 500; line-height: 31px;
  }
  .intro__line { display: block; white-space: nowrap; }
  .intro__line--full { text-align: justify; text-align-last: justify; }
  .intro__line--last { text-align: center; }

  .books { position: absolute; left: 636px; top: 285px; width: 528px; height: 322px; }

  .footer {
    position: absolute; left: 0; top: 607px; width: 1200px; height: 69px;
    background: var(--footer-navy); color: var(--white);
  }
  .footer__label, .footer__web {
    position: absolute; top: 24px; font-size: 17px; font-weight: 300; letter-spacing: 3.4px;
  }
  .footer__label { left: 117px; }
  .footer__web { left: 825px; }
  .footer__social { position: absolute; left: 530px; top: 26px; display: flex; gap: 14px; }
  .footer__social span { font-size: 13px; font-weight: 500; }
</style>
</head>
<body>
<div class="page">
  <div class="portrait" role="img" aria-label="Black and white portrait photo of the author on a blue circle"></div>

  <div class="name-card">
    <p class="name-card__name">Marlo Quinn<span class="accent">.</span></p>
    <p class="name-card__role">PUBLICIST</p>
  </div>

  <section class="intro">
    <h1 class="intro__title">Learn more about my work<span class="accent">!</span></h1>
    <p class="intro__text">
      <span class="intro__line intro__line--full">Lorem ipsum dolor sit amet, consectetur adi-</span>
      <span class="intro__line intro__line--full">piscing elit, sed do eiusmod tempor incididunt</span>
      <span class="intro__line intro__line--last">ut labore et dolore magna aliqua quis ipsum.</span>
    </p>
  </section>

  <svg class="books" viewBox="0 0 528 322" role="img" aria-label="Two book covers by the author, shown as a stacked pair">
    <defs>
      <linearGradient id="backCover" x1="0" y1="0" x2="1" y2="1">
        <stop offset="0" stop-color="#9fb3c9"/>
        <stop offset="0.5" stop-color="var(--book-light)"/>
        <stop offset="1" stop-color="var(--book-mid)"/>
      </linearGradient>
      <linearGradient id="frontCover" x1="0" y1="0" x2="0" y2="1">
        <stop offset="0" stop-color="#f4f6f9"/>
        <stop offset="0.45" stop-color="var(--book-light)"/>
        <stop offset="0.6" stop-color="var(--book-mid)"/>
        <stop offset="1" stop-color="var(--book-deep)"/>
      </linearGradient>
    </defs>
    <polygon points="0,149 212,2 268,59 228,322 150,322" fill="url(#backCover)"/>
    <polygon points="213,61 479,68 527,322 226,322" fill="url(#frontCover)"/>
    <polygon points="213,61 220,62 232,322 226,322" fill="#cfd6df"/>
  </svg>

  <footer class="footer">
    <span class="footer__label">MORE INFORMATION:</span>
    <div class="footer__social">
      <span>Pulse</span><span>Relay</span><span>Frame</span>
    </div>
    <span class="footer__web">BRANDFIELDNOTES.COM</span>
  </footer>
</div>
</body>
</html>
```